Wirenexa

I'm looking to much improve our current website wirenexa.com
Updates

Low design quality

Target Market(s)

Commercial clients (Not-Residentials)

Industry/Entity Type

Office buildings and Industrial clients

Coding

Coded - Design and coding required

Number of Pages Required

5+ page

Requirements
Must have
• Very professional structured low voltage cabling projects for Wi-Fi, Audio/Video conference rooms, Access Control systems, CCTV.

```html
<!DOCTYPE html>
<html lang="en">
<head>
<meta charset="UTF-8">
<title>Wirenexa — About Us</title>
<link href="https://fonts.googleapis.com/css2?family=Inter:wght@400;500;600;700;800;900&family=JetBrains+Mono:wght@400;700;800&display=swap" rel="stylesheet">
<style>
  :root {
    --bg-page: #0b0b0b;
    --bg-hero: #141414;
    --bg-card: #141414;
    --line: #2a2a2a;
    --red: #d32f27;
    --white: #ffffff;
    --text: #b8b8b8;
    --text-strong: #cfcfcf;
  }
  * { margin: 0; padding: 0; box-sizing: border-box; }
  html, body { width: 1023px; height: 1200px; overflow: hidden; }
  body {
    position: relative;
    background: var(--bg-page);
    font-family: "Inter", sans-serif;
    color: var(--text);
  }
  .brand { display: flex; align-items: center; gap: 6px; position: absolute; }
  .brand-mark { background: var(--red); display: block; }
  .brand-name { color: var(--white); font-weight: 800; letter-spacing: -0.02em; }

  .site-header {
    position: absolute; left: 0; top: 0; width: 1023px; height: 57px;
    background: var(--bg-page); border-bottom: 1px solid var(--line);
  }
  .site-header .brand { left: 74px; top: 12px; height: 28px; }
  .site-header .brand-mark { width: 28px; height: 28px; }
  .site-header .brand-name { font-size: 21px; }
  .main-nav a {
    position: absolute; top: 22px; font-size: 10px; font-weight: 500;
    letter-spacing: 0.05em; color: var(--white); text-decoration: none; line-height: 13px;
  }
  .main-nav .is-active { color: var(--red); }
  .nav-cta {
    position: absolute; left: 797px; top: 12px; width: 104px; height: 33px;
    background: var(--red); color: var(--white); font-size: 10px; font-weight: 500;
    letter-spacing: 0.05em; display: flex; align-items: center; justify-content: center;
  }
  .theme-toggle { position: absolute; left: 929px; top: 21px; width: 14px; height: 14px; }

  .hero {
    position: absolute; left: 0; top: 57px; width: 1023px; height: 307px;
    background: var(--bg-hero); border-bottom: 1px solid var(--line);
  }
  .hero-title {
    position: absolute; left: 73px; top: 68px; font-weight: 900; font-size: 56px;
    line-height: 57px; letter-spacing: -0.045em; color: var(--white); text-transform: uppercase;
  }
  .hero-title .accent { color: var(--red); display: block; }
  .hero-lead {
    position: absolute; left: 74px; top: 194px; width: 420px;
    font-size: 14.5px; line-height: 22.7px; color: var(--text);
  }

  .why {
    position: absolute; left: 74px; top: 432px; width: 416px;
  }
  .why h2 { color: var(--white); font-size: 23px; font-weight: 700; letter-spacing: -0.01em; line-height: 28px; }
  .why p { font-size: 11.6px; line-height: 18.3px; color: var(--text); }
  .why strong { color: var(--text-strong); font-weight: 700; }
  .why .p1 { margin-top: 20px; }
  .why .p2 { margin-top: 17px; }
  .why h3 { margin-top: 38px; color: var(--white); font-size: 17.5px; font-weight: 700; line-height: 22px; }
  .why .p3 { margin-top: 14px; }

  .stat-card {
    position: absolute; left: 534px; width: 415px; height: 96px;
    background: var(--bg-card); border: 1px solid var(--line);
  }
  .stat-card.one { top: 432px; }
  .stat-card.two { top: 551px; }
  .stat-number {
    position: absolute; left: 24px; top: 22px; font-family: "JetBrains Mono", monospace;
    font-weight: 800; font-size: 44px; line-height: 50px; color: var(--red); letter-spacing: -0.02em;
  }
  .stat-title { position: absolute; left: 155px; top: 26px; font-size: 17.5px; font-weight: 700; color: var(--white); line-height: 22px; }
  .stat-text { position: absolute; left: 155px; top: 58px; font-size: 10.5px; color: var(--text); line-height: 14px; }

  .site-footer {
    position: absolute; left: 0; top: 877px; width: 1023px; height: 323px;
    border-top: 1px solid var(--line);
  }
  .site-footer .brand { left: 74px; top: 46px; height: 43px; gap: 7px; }
  .site-footer .brand-mark { width: 43px; height: 43px; }
  .site-footer .brand-name { font-size: 32px; }
  .footer-about {
    position: absolute; left: 74px; top: 110px; width: 218px;
    font-size: 11.6px; line-height: 18.2px; color: var(--text);
  }
  .footer-col { position: absolute; top: 52px; }
  .footer-col h4 { color: var(--white); font-size: 10px; font-weight: 700; line-height: 13px; text-transform: uppercase; }
  .footer-col ul { list-style: none; margin-top: 16px; }
  .footer-col li { font-size: 10.5px; line-height: 13px; margin-bottom: 8.3px; }
  .footer-links { left: 523px; }
  .footer-links li { color: var(--white); }
  .footer-contact { left: 747px; }
  .footer-contact li { color: var(--text); }
  .footer-contact .mono { font-family: "JetBrains Mono", monospace; font-size: 10px; }
  .footer-bottom {
    position: absolute; left: 74px; top: 263px; width: 875px; border-top: 1px solid var(--line);
    display: flex; justify-content: space-between; padding-top: 24px;
    font-size: 9px; color: var(--text); line-height: 12px;
  }
  .legal-links span { margin-left: 11px; }
</style>
</head>
<body>
  <header class="site-header">
    <div class="brand">
      <span class="brand-mark"></span>
      <span class="brand-name">Wirenexa</span>
    </div>
    <nav class="main-nav">
      <a style="left:592px">HOME</a>
      <a style="left:646px" class="is-active">ABOUT US</a>
      <a style="left:723px">SERVICES</a>
    </nav>
    <div class="nav-cta">CONTACT US</div>
    <svg class="theme-toggle" viewBox="0 0 24 24" fill="none" stroke="#ffffff" stroke-width="2" stroke-linecap="round" stroke-linejoin="round"><path d="M21 12.8A9 9 0 1 1 11.2 3a7 7 0 0 0 9.8 9.8z"/></svg>
  </header>

  <section class="hero">
    <h1 class="hero-title">Your trusted<span class="accent">cabling partner.</span></h1>
    <p class="hero-lead">Wirenexa is a leading infrastructure cabling company dedicated to building, managing, securing, and supporting Information Technology infrastructure.</p>
  </section>

  <section class="why">
    <h2>Why Choose Wirenexa?</h2>
    <p class="p1"><strong>Decades of Experience:</strong> With decades of experience in Information Technology, Wirenexa brings unparalleled expertise to every project. Our seasoned professionals have the knowledge and skills to deliver efficient, results-oriented solutions tailored to your specific needs.</p>
    <p class="p2"><strong>Top-Notch Customer Service:</strong> At Wirenexa, customer satisfaction is our top priority. We pride ourselves on delivering top-notch customer service and support to ensure that your technology needs are met with excellence and professionalism.</p>
    <h3>Nationwide Reach &amp; Diverse Clientele</h3>
    <p class="p3">Since our founding in 1994, we have successfully assisted hundreds of companies and organizations nationwide. Wirenexa serves a diverse clientele, including small, mid-size, and larger businesses across various industries. Many of our customer relationships have lasted for more than two decades, a testament to the quality and reliability of our services.</p>
  </section>

  <div class="stat-card one">
    <div class="stat-number">1994</div>
    <div class="stat-title">Year Established</div>
    <div class="stat-text">Decades of proven industry experience.</div>
  </div>
  <div class="stat-card two">
    <div class="stat-number">100+</div>
    <div class="stat-title">Enterprise Clients</div>
    <div class="stat-text">Trusted by organizations nationwide.</div>
  </div>

  <footer class="site-footer">
    <div class="brand">
      <span class="brand-mark"></span>
      <span class="brand-name">Wirenexa</span>
    </div>
    <p class="footer-about">Wirenexa is a local group of IT professionals, dedicated to fast, reliable and honest service. No job is too big or too small, get in touch today for solutions to all your IT infrastructure needs!</p>
    <div class="footer-col footer-links">
      <h4>Quick Links</h4>
      <ul><li>About Us</li><li>Services</li><li>Contact</li></ul>
    </div>
    <div class="footer-col footer-contact">
      <h4>Reach Us</h4>
      <ul>
        <li class="mono">National: (888) 555-0142</li>
        <li class="mono">Local: 703-555-0187</li>
        <li>sales@wirenexa.com</li>
      </ul>
    </div>
    <div class="footer-bottom">
      <span>© 2026 Wirenexa. All rights reserved.</span>
      <span class="legal-links"><span>Privacy Policy</span><span>Terms of Service</span></span>
    </div>
  </footer>
</body>
</html>
```